tundra basics anti snore device

The item is a silicone anti snore device that goes into your nostrils. I need an attractive descriptive design. If a photo from pixelharbor or a free and clear without copyright issue can be used to photo shop in the product that would be awesome. The product is pretty much identical to the following item which I've attached a link http://www.brivomart.example/Snoring-AeroFlix-Sleep-Apnea-Device/dp/Q77K2LMZ04/ref=sr_1_1?ie=UTF8&qid=1409110329&sr=8-1&keywords=aeroflix. There are several pictures of the different angles as well as the instructions. I like this packaging but I obviously need to change it around. i think it could be a good reference though.

There is a document for the back instructions. Please show me the back design as well.

Target Market(s)

adults mostly men. should have "sleepy colors"

Industry/Entity Type

Shop

Font styles to use
Serif

Colors
33b7a4
cadf83
85cae6
faee3e
e34197

Requirements
Must have
• sharp with an image
Should not have
• name of "aeroflix" anywhere on it

```html
<!DOCTYPE html>
<html lang="en">
<head>
<meta charset="utf-8">
<title>Tundra Basics Anti-Snoring Aid</title>
<link rel="stylesheet" href="https://fonts.googleapis.com/css2?family=Tinos:ital,wght@0,400;1,700&family=Roboto+Condensed:wght@400&display=swap">
<style>
  :root {
    --page: #ffffff;
    --teal-light: #bff0f5;
    --teal: #5fd0dc;
    --teal-deep: #2fa9bb;
    --swoosh-dark: #1d2430;
    --lilac: #efe6f8;
    --lilac-deep: #dccdf0;
    --rule: #7fa3b8;
    --navy: #243064;
    --ink: #141414;
    --pink: #e0609a;
    --blue: #3a4fb0;
    --wave-blue: #3c54b8;
    --hair: #8a6a52;
    --skin: #e2b9a0;
    --bedding: #f7f5f6;
    --device: #dfe1e4;
  }
  * { margin: 0; padding: 0; box-sizing: border-box; }
  html, body {
    width: 993px; height: 1200px; overflow: hidden;
    background: var(--page);
  }
  .canvas { position: relative; width: 993px; height: 1200px; }
  .card {
    position: absolute; left: 83px; top: 18px; width: 810px; height: 1167px;
    border-radius: 64px; overflow: hidden;
    background:
      radial-gradient(ellipse 420px 260px at 20% 96%, rgba(230,190,235,0.75), transparent 70%),
      radial-gradient(ellipse 360px 240px at 92% 92%, rgba(235,200,240,0.6), transparent 70%),
      linear-gradient(180deg, #f6f2fb 0%, var(--lilac) 40%, #f3eefa 70%, var(--lilac-deep) 100%);
    box-shadow: 0 6px 14px rgba(0,0,0,0.35);
  }
  .card-shapes { position: absolute; inset: 0; }
  .brand {
    position: absolute; left: 0; width: 100%; top: 195px;
    font-family: "Tinos", serif; font-size: 66px; color: var(--navy);
    display: flex; justify-content: center; align-items: center; gap: 18px;
  }
  .brand-dot { width: 22px; height: 22px; border-radius: 50%; background: var(--teal-deep); }
  .rules { position: absolute; left: 12px; width: 773px; top: 307px; }
  .rules span { display: block; height: 2px; background: var(--rule); margin-bottom: 12px; }
  .product-title {
    position: absolute; left: 407px; top: 334px;
    font-family: "Tinos", serif; font-style: italic; font-weight: 700;
    font-size: 28px; color: var(--navy);
  }
  .product-names {
    position: absolute; left: 408px; top: 378px; list-style: none;
    font-family: "Roboto Condensed", sans-serif; font-size: 32px; line-height: 41px; color: var(--navy);
  }
  .family-photo {
    position: absolute; left: 292px; top: 520px; width: 515px; height: 280px;
    background:
      radial-gradient(ellipse 70px 60px at 28% 28%, var(--skin), transparent 75%),
      radial-gradient(ellipse 60px 55px at 45% 45%, var(--skin), transparent 75%),
      radial-gradient(ellipse 65px 60px at 62% 32%, #efcdb5, transparent 75%),
      radial-gradient(ellipse 70px 65px at 82% 28%, var(--skin), transparent 75%),
      linear-gradient(180deg, var(--hair) 0%, #c9a58c 30%, #eadbd3 55%, var(--bedding) 75%, #ffffff 100%);
    -webkit-mask-image: radial-gradient(ellipse 52% 52% at 55% 50%, #000 60%, transparent 100%);
    mask-image: radial-gradient(ellipse 52% 52% at 55% 50%, #000 60%, transparent 100%);
  }
  .device-photo {
    position: absolute; left: 630px; top: 805px; width: 145px; height: 150px;
    background: linear-gradient(180deg, #f4f5f6 0%, var(--device) 55%, #c3c7cc 100%);
    -webkit-mask-image: radial-gradient(ellipse 50% 50% at 50% 50%, #000 55%, transparent 100%);
    mask-image: radial-gradient(ellipse 50% 50% at 50% 50%, #000 55%, transparent 100%);
  }
  .claims {
    position: absolute; left: 389px; list-style: none;
    font-family: "Tinos", serif; font-size: 16.5px; line-height: 21px; color: var(--ink);
  }
  .claims-fit { top: 805px; }
  .claims-doctor { top: 935px; }
  .claims .lead-pink { color: var(--pink); }
  .claims .lead-blue { color: var(--blue); }
</style>
</head>
<body>
<div class="canvas">
  <div class="card">
    <svg class="card-shapes" width="810" height="1167" viewBox="0 0 810 1167">
      <defs>
        <linearGradient id="tealBand" x1="0" y1="0" x2="0" y2="1">
          <stop offset="0" stop-color="var(--teal-light)"/>
          <stop offset="0.55" stop-color="var(--teal)"/>
          <stop offset="1" stop-color="var(--teal-deep)"/>
        </linearGradient>
        <linearGradient id="tealFoot" x1="0" y1="0" x2="0" y2="1">
          <stop offset="0" stop-color="#9fe6ee"/>
          <stop offset="1" stop-color="var(--teal-deep)"/>
        </linearGradient>
      </defs>
      <path class="header-swoosh" d="M20 20 Q405 175 790 40 L790 62 Q405 200 20 44 Z" fill="var(--swoosh-dark)"/>
      <path class="header-band" d="M0 0 H810 V40 Q405 185 0 40 Z" fill="url(#tealBand)"/>
      <path class="footer-wave-grey" d="M330 1167 Q620 1080 810 1060 L810 1167 Z" fill="#c9d3ea" opacity="0.8"/>
      <path class="footer-wave-blue" d="M0 1030 Q420 990 640 1167 L600 1167 Q400 1020 0 1048 Z" fill="var(--wave-blue)"/>
      <path class="footer-band" d="M0 1048 Q400 1020 600 1167 L0 1167 Z" fill="url(#tealFoot)"/>
    </svg>

    <div class="brand"><span class="brand-dot"></span>Tundra Basics</div>
    <div class="rules"><span></span><span></span></div>

    <h1 class="product-title">Anti-Snoring Aid</h1>
    <ul class="product-names">
      <li>AntiRonquido</li>
      <li>Anti-Schnrach-Mittel</li>
      <li>Produit Anti-Ronflement</li>
      <li>Anti-Snurkmiddel</li>
    </ul>

    <div class="family-photo" role="img" aria-label="Photo of a family of four sleeping together under white bedding"></div>
    <div class="device-photo" role="img" aria-label="Photo of the white silicone nasal anti-snoring device"></div>

    <ul class="claims claims-fit">
      <li class="lead-pink">Fits any nose</li>
      <li>se adapta a cada nariz</li>
      <li>passt fur jede nase</li>
      <li>convient a chaque nez</li>
      <li>past in elke neus</li>
    </ul>
    <ul class="claims claims-doctor">
      <li class="lead-blue">Recommended by ENT doctors</li>
      <li>Recomendado por&nbsp; otorrinos</li>
      <li>Von HNO-Arzten empfohlen</li>
      <li>Recommande par des medecins o</li>
      <li>aanbevolen door KNO artsen</li>
    </ul>
  </div>
</div>
</body>
</html>
```